Hallvard
Veneer Technology
Hallvard - Agriculture
Creative Brief
Agriculture
http://hallvard-veneertechnology.example
We have 4 different product lines.
1. Stone-Veneer
2.Sonic-Paneltrim
3.Plexard
4.Moravelt
We do not installl any products. We just distribute them to architects, companies, builders, ect.
The stone can be made for any products. From laptops, countertops, "wall paper", notebooks, smart car, sinks, ect.
Dislikes: -it's hard to see what our company is -appearance -professionalism -pictures -it's not appealing
Nature
Gray, white and blacks
Blues
Red (Nothing too bright!)
below header
http://www.brevicott.example
http://www.folmaneq.example/
http://4plank.example

```html
<!DOCTYPE html>
<html lang="en">
<head>
<meta charset="utf-8">
<title>Hallvard Veneer Technology</title>
<link href="https://fonts.googleapis.com/css2?family=Arimo:wght@400;700&display=swap" rel="stylesheet">
<style>
:root{
  --red:#b3122a;
  --red-dark:#7e0c1d;
  --red-light:#d42a40;
  --ink:#2b2b2b;
  --muted:#666;
  --blue:#1f6fb2;
  --panel:#f1f1f1;
  --line:#d5d5d5;
  --tab:#111;
  --tab-text:#f2c21b;
}
*{box-sizing:border-box;margin:0;padding:0}
html,body{width:1200px;height:1021px;overflow:hidden}
body{font-family:"Arimo",Arial,sans-serif;color:var(--ink);background:linear-gradient(#f7f7f7,#e4e4e4);position:relative}
.abs{position:absolute}

.brand{left:150px;top:26px;display:flex;align-items:center;gap:12px}
.brand-mark{width:44px;height:60px;background:var(--red)}
.brand-name{color:var(--red);font-weight:700;font-size:27px;line-height:30px}

.phone{left:830px;top:32px;display:flex;align-items:center;gap:14px;font-size:34px;color:#333}
.search{left:885px;top:103px;width:205px;height:24px;border:1px solid #bbb;background:#fff;font-size:12px;color:#888;padding:4px 8px}
.search-btn{position:absolute;right:-1px;top:-1px;width:26px;height:24px;background:#9a9a9a}

.nav-ribbon{left:40px;top:148px}
.nav{left:114px;top:151px;width:977px;height:58px;display:flex;align-items:center}
.nav a{color:#fff;text-decoration:none;font-size:22px;height:100%;display:flex;align-items:center;justify-content:center;border-right:1px solid rgba(255,255,255,.35)}
.nav a:last-child{border-right:0}

.page{left:114px;top:209px;width:977px;height:748px;background:#fff;box-shadow:0 2px 6px rgba(0,0,0,.15)}

.slider{left:134px;top:237px;width:937px;height:286px;background:linear-gradient(135deg,#b8a68e,#9a8670 45%,#c5b59e);}
.slider-tab{position:absolute;top:0;width:36px;height:286px;background:var(--tab);color:var(--tab-text);font-size:16px}
.slider-tab span{position:absolute;left:50%;top:12px;writing-mode:vertical-rl;transform:translateX(-50%) rotate(180deg);white-space:nowrap}
.slider-tab b{position:absolute;bottom:10px;left:0;right:0;text-align:center;font-size:18px;font-weight:400}
.slider-tab.right span{transform:translateX(-50%)}

.card{top:571px;width:299px;height:195px;background:var(--panel);border:1px solid var(--line);border-radius:4px}
.card-head{position:absolute;left:10px;top:-4px;width:205px;height:34px;background:#fff;border:1px solid var(--line);display:flex;align-items:center;gap:8px;padding-left:10px;color:var(--blue);font-size:22px}
.card-head i{width:16px;height:16px;border-radius:50%;border:2px solid #777;display:inline-block}
.card-body{position:absolute;left:16px;top:46px;width:170px;font-size:13px;line-height:19px;color:#444}
.card-art{position:absolute;right:16px;top:60px;width:80px;height:90px;border-radius:8px}
.more{position:absolute;right:30px;bottom:10px;font-size:13px;color:#444}

.carousel{left:134px;top:795px;width:937px;height:142px;background:var(--panel);border:1px solid var(--line);border-radius:4px}
.arrow{position:absolute;top:59px;width:24px;height:24px;border-radius:50%;background:#111}
.thumb{position:absolute;top:16px;width:155px;height:110px}

.footer-mark{left:140px;top:980px;display:flex;align-items:center;gap:6px;color:#c8c8c8;font-weight:700;font-size:15px;line-height:16px}
.footer-mark i{width:14px;height:22px;background:#d0d0d0}
.footer-links{right:40px;top:983px;font-size:13px;color:#333;display:flex;gap:8px}
.footer-links span.sep{color:#999}
.copy{right:40px;top:1002px;font-size:13px;color:#555}
.copy em{font-style:normal;color:var(--red)}
</style>
</head>
<body>

<div class="abs brand">
  <div class="brand-mark"></div>
  <div class="brand-name">Hallvard<br>veneer technology</div>
</div>

<div class="abs phone">
  <svg width="60" height="46" viewBox="0 0 60 46"><path d="M4 14c0-8 52-8 52 0v6h-12v-5c-6-2-22-2-28 0v5H4z" fill="#222"/><path d="M14 22h32l8 20H6z" fill="#333"/><circle cx="30" cy="32" r="7" fill="#888"/></svg>
  <span>888-555-0192</span>
</div>
<div class="abs search">Search...<div class="search-btn"></div></div>

<svg class="abs nav-ribbon" width="1140" height="80" viewBox="0 0 1140 80">
  <path d="M11 12h80v58H11l22-29z" fill="var(--red-dark)"/>
  <path d="M1131 12h-80v58h80l-22-29z" fill="var(--red-dark)"/>
  <path d="M74 61l17 9V61z" fill="#4d0711"/>
  <path d="M1068 61l-17 9V61z" fill="#4d0711"/>
  <rect x="74" y="3" width="977" height="58" fill="var(--red)"/>
  <rect x="74" y="3" width="977" height="10" fill="var(--red-light)"/>
</svg>
<nav class="abs nav">
  <a style="width:110px">Home</a>
  <a style="width:150px">News</a>
  <a style="width:170px">Products</a>
  <a style="width:345px">Corporate Social Responsibility</a>
  <a style="width:202px">Contact Us</a>
</nav>

<div class="abs page"></div>

<div class="abs slider" role="img" aria-label="Close-up of cracked natural stone veneer surface">
  <div class="slider-tab" style="left:32px"><span>Stone-Veneer</span><b>1</b></div>
  <div class="slider-tab right" style="left:782px"><span>Sonic-Paneltrim</span><b>2</b></div>
  <div class="slider-tab right" style="left:826px"><span>Plexard</span><b>3</b></div>
  <div class="slider-tab right" style="left:870px"><span>Moravelt</span><b>4</b></div>
</div>

<div class="abs card" style="left:134px">
  <div class="card-head"><i></i>Sample Heading</div>
  <p class="card-body">Lorem ipsum dolor sit amet, consectetur adipiscing elit. Nullam a libero non nunc porttitor varius. Vivamus neque est.</p>
  <div class="card-art" role="img" aria-label="Bar chart illustration" style="background:linear-gradient(135deg,#8ec45a,#f2b33d 50%,#3d79c9)"></div>
  <span class="more">» Read More</span>
</div>
<div class="abs card" style="left:453px">
  <div class="card-head"><i></i>Sample Heading</div>
  <p class="card-body">Lorem ipsum dolor sit amet, consectetur adipiscing elit. Nullam a libero non nunc porttitor varius. Vivamus neque est.</p>
  <div class="card-art" role="img" aria-label="Globe with arrows illustration" style="border-radius:50%;background:radial-gradient(circle at 40% 35%,#7fc6f2,#1f6fb2 70%)"></div>
  <span class="more">» Read More</span>
</div>
<div class="abs card" style="left:772px">
  <div class="card-head"><i></i>Contact Us</div>
  <p class="card-body"><b>Address:</b><br>2450 Quarry Lane<br>Eastbrook, MD 21990<br><b>Fax Number:</b><br>410-555-0147</p>
  <div class="card-art" role="img" aria-label="Envelope with letter illustration" style="background:linear-gradient(135deg,#e8f1fb,#7fb3e0)"></div>
  <span class="more">» Read More</span>
</div>

<div class="abs carousel">
  <span class="arrow" style="left:16px"><svg width="24" height="24"><path d="M14 7l-5 5 5 5" stroke="#fff" stroke-width="2" fill="none"/></svg></span>
  <div class="thumb" role="img" aria-label="Living room interior" style="left:52px;background:linear-gradient(#d9d2c6,#8a6a4c)"></div>
  <div class="thumb" role="img" aria-label="Kitchen interior at night" style="left:222px;background:linear-gradient(#4a3a2c,#c89a5e)"></div>
  <div class="thumb" role="img" aria-label="Bright room with windows" style="left:392px;background:linear-gradient(#f2f2ee,#b9b3a8)"></div>
  <div class="thumb" role="img" aria-label="Modern lounge interior" style="left:562px;background:linear-gradient(#3a2f28,#9b7b5c)"></div>
  <div class="thumb" role="img" aria-label="Wooden kitchen cabinets" style="left:732px;background:linear-gradient(#7a4a26,#c9874a)"></div>
  <span class="arrow" style="right:16px"><svg width="24" height="24"><path d="M10 7l5 5-5 5" stroke="#fff" stroke-width="2" fill="none"/></svg></span>
</div>

<div class="abs footer-mark"><i></i><span>Hallvard<br>veneer technology</span></div>
<div class="abs footer-links">
  <span>Home</span><span class="sep">|</span><span>News</span><span class="sep">|</span><span>Sonic-Paneltrim</span><span class="sep">|</span><span>Stone-Veneer</span><span class="sep">|</span><span>Moravelt</span><span class="sep">|</span><span>Contact Us</span><span class="sep">|</span><span>Site Map</span>
</div>
<div class="abs copy">Copyright © 2011 <em>Hallvard veneer technology</em>. All rights reserved.</div>

</body>
</html>
```